Land Development Company Website Redesign

We are looking for a fresh design for our website. The content will remain 90% the same.

We really like the layout style of www.kelvarno.com.

We have attached our current site for content.

Industry/Entity Type

Real Estate Development

Coding

Coded - Design and coding required

Number of Pages Required

5+ page

Font styles to use
Sans Serif

Requirements
Must have
• Consistent feel across all the pages. Visually appealing and simple layout design that can be viewed on a mobile device and browser.

```html
<!DOCTYPE html>
<html lang="en">
<head>
<meta charset="utf-8">
<title>Ridgemere Communities</title>
<link href="https://fonts.googleapis.com/css2?family=Roboto+Condensed:wght@400;700&family=Open+Sans:ital,wght@0,400;0,600;1,400&family=Great+Vibes&display=swap" rel="stylesheet">
<style>
:root{
  --gold:#c9a063;
  --ink:#222;
  --text:#555;
  --nav:#1c1c1c;
  --footer:#2f2f2f;
  --bar:#111;
  --white:#fff;
  --line:#d8d8d8;
}
*{margin:0;padding:0;box-sizing:border-box}
html,body{width:1200px;height:4432px;overflow:hidden}
body{position:relative;background:var(--white);font-family:"Open Sans",sans-serif;color:var(--text)}
section,header,footer,nav{position:absolute;left:0;width:1200px}
.heading{font-family:"Roboto Condensed",sans-serif;font-weight:700;font-size:40px;text-align:center;color:var(--ink);letter-spacing:1px}
.heading .accent{color:var(--gold)}
.script{font-family:"Great Vibes",cursive;font-size:30px;text-align:center;color:var(--ink)}
.btn{display:inline-block;background:var(--gold);color:var(--white);font-family:"Roboto Condensed",sans-serif;font-size:18px;padding:12px 34px;letter-spacing:1px}
.photo{position:absolute}
.arrow{position:absolute;width:36px;height:36px;display:flex;align-items:center;justify-content:center}

/* hero */
.hero{top:0;height:660px;background:linear-gradient(180deg,#8b7aa8 0%,#b59ab7 25%,#c8b8a8 45%,#a08a6c 70%,#4e4336 100%)}
.brand{position:absolute;top:72px;left:0;width:1200px;display:flex;justify-content:center;align-items:center;gap:14px}
.brand-mark{width:44px;height:44px;background:#1b1b1b}
.brand-name{font-family:"Roboto Condensed",sans-serif;font-weight:700;font-size:30px;color:var(--white);letter-spacing:3px}
.main-nav{top:660px;height:48px;background:var(--nav);display:flex;justify-content:center;align-items:center;gap:38px}
.main-nav a{font-family:"Roboto Condensed",sans-serif;font-size:18px;color:var(--white);text-decoration:none}
.main-nav a.active{color:var(--gold)}

/* about */
.about{top:708px;height:392px;text-align:center}
.about .heading{margin-top:60px}
.about .script{margin-top:6px}
.about p{width:780px;margin:24px auto 0;font-size:15px;line-height:24px}
.about .btn{margin-top:32px}

/* what's new */
.news{top:1100px;height:520px;background:linear-gradient(180deg,#3e4a44 0%,#5a6258 45%,#6f6a5c 70%,#3a3a36 100%)}
.news::after{content:"";position:absolute;inset:0;background:rgba(0,0,0,.35)}
.news>*{position:relative;z-index:1}
.news .heading{color:var(--white);margin-top:66px}
.quote{width:860px;margin:80px auto 0;font-family:"Open Sans",sans-serif;font-style:italic;font-size:28px;line-height:40px;text-align:center;color:var(--white);text-transform:uppercase}
.quote-author{text-align:center;margin-top:30px;font-size:17px;color:var(--white)}
.news .arrow{position:absolute;background:#222;top:396px}

/* maps */
.maps{top:1620px;height:560px}
.maps .heading{margin-top:60px}
.maps .script{font-size:28px}
.maps .arrow{background:#666;top:318px}

/* builders */
.builders{top:2180px;height:740px;background:linear-gradient(135deg,#3a2a1e 0%,#6b4a32 40%,#4a3424 70%,#2a1e16 100%)}
.builders::after{content:"";position:absolute;inset:0;background:rgba(0,0,0,.45)}
.builders>*{position:relative;z-index:1}
.builders .heading{margin-top:46px;color:var(--white)}
.builders .builder{position:absolute;top:168px;width:430px;color:var(--white)}
.builder h3{font-family:"Roboto Condensed",sans-serif;font-weight:400;font-size:34px;letter-spacing:1px;white-space:nowrap}
.builder .photo{position:relative;display:block;width:128px;height:100px;margin:22px auto 0;background:linear-gradient(135deg,#e6b8a6,#c88878)}
.builder p{font-size:13px;line-height:21px;margin-top:20px;color:#eee}
.builder p+p{margin-top:14px}
.builders .cta{position:absolute;top:582px;left:0;width:1200px;text-align:center}
.builders .hurry{position:absolute;top:660px;left:0;width:1200px;text-align:center;font-family:"Roboto Condensed",sans-serif;font-size:20px;color:var(--white);letter-spacing:1px}
.hurry .accent{color:var(--gold)}

/* lifestyle */
.lifestyle{top:2920px;height:640px}
.lifestyle .heading{margin-top:42px}
.filters{display:flex;justify-content:center;gap:10px;margin-top:14px}
.filters span{font-size:13px;padding:4px 14px;border:1px solid var(--line);color:var(--text)}
.filters span.active{background:#444;color:var(--white);border-color:#444}
.gallery .photo{width:240px;height:180px}

/* contact form */
.enquiry{top:3560px;height:532px;background:linear-gradient(90deg,#4a5a70 0%,#8a97a6 30%,#c9ccd0 55%,#7a8290 80%,#3e4450 100%)}
.enquiry::after{content:"";position:absolute;inset:0;background:rgba(255,255,255,.25)}
.enquiry>*{position:relative;z-index:1}
.enquiry .heading{margin-top:44px;color:#2a2a2a}
.enquiry .script{margin-top:58px;color:var(--white);font-size:32px}
.enquiry .form{position:absolute;top:220px;left:88px;width:1024px;height:170px}
.field{position:absolute;left:0;width:504px;height:44px;border:1px solid rgba(255,255,255,.8);background:rgba(255,255,255,.15);color:var(--white);font-size:14px;padding:12px 14px}
.field.message{left:532px;top:0;width:492px;height:160px}
.enquiry .cta{position:absolute;top:416px;left:0;width:1200px;text-align:center}

/* footer */
.contact{top:4092px;height:280px;background:var(--footer);text-align:center;color:#ccc}
.contact .heading{margin-top:44px;color:var(--white)}
.social{display:flex;justify-content:center;gap:10px;margin-top:40px}
.social span{width:36px;height:36px;background:#666;border-radius:3px}
.social span:first-child{background:#3b5a98}
.contact p{font-size:14px;line-height:22px;margin-top:14px}
.contact p+p{margin-top:0}
.contact .accent{color:var(--gold)}
.legal{top:4372px;height:60px;background:var(--bar);text-align:center;line-height:60px;font-size:13px;color:#aaa}
.legal .accent{color:var(--gold)}
</style>
</head>
<body>

<header class="hero" role="img" aria-label="Photograph of a large stone estate home at dusk with a patio and fire pit">
  <div class="brand"><span class="brand-mark"></span><span class="brand-name">RIDGEMERE</span></div>
</header>

<nav class="main-nav">
  <a class="active">HOME</a><a>WHAT'S NEW</a><a>MAPS</a><a>OUR BUILDERS</a><a>LIFE STYLE</a><a>CONTACT</a>
</nav>

<section class="about">
  <h2 class="heading">ABOUT <span class="accent">RIDGEMERE COMMUNITIES</span></h2>
  <div class="script">Lorem ipsum is a dummy text</div>
  <p>Lorem Ipsum is simply dummy text of the printing and typesetting industry. Lorem Ipsum has been the industry's standard dummy text ever since the 1500s, when an unknown printer took a galley of type and scrambled it to make a type specimen book. It has survived not only five centuries, but also the leap into electronic typesetting, remaining essentially unchanged. It was popularised in the 1960s with the release of Letraset sheets containing Lorem Ipsum passages.</p>
  <span class="btn">READ MORE</span>
</section>

<section class="news" role="img" aria-label="Photograph of a community entrance gate with trees at evening">
  <h2 class="heading">WHAT'S <span class="accent">NEW</span></h2>
  <p class="quote">" Lorem Ipsum is simply dummy text of the printing and typesetting industry. "</p>
  <p class="quote-author">- Martin Cole</p>
  <span class="arrow" style="left:560px"><svg width="14" height="14" viewBox="0 0 14 14"><path d="M9 2 4 7l5 5" stroke="#fff" stroke-width="2" fill="none"/></svg></span>
  <span class="arrow" style="left:604px"><svg width="14" height="14" viewBox="0 0 14 14"><path d="M5 2l5 5-5 5" stroke="#fff" stroke-width="2" fill="none"/></svg></span>
</section>

<section class="maps">
  <h2 class="heading">MAPS</h2>
  <div class="script">Regional</div>
  <div class="photo" style="left:352px;top:200px;width:496px;height:280px;background:linear-gradient(180deg,#b8a896 0%,#8a7a6a 55%,#c8c0b4 100%)" role="img" aria-label="Illustration of a two-storey family house with a double garage"></div>
  <span class="arrow" style="left:162px"><svg width="14" height="14" viewBox="0 0 14 14"><path d="M9 2 4 7l5 5" stroke="#fff" stroke-width="2" fill="none"/></svg></span>
  <span class="arrow" style="left:1002px"><svg width="14" height="14" viewBox="0 0 14 14"><path d="M5 2l5 5-5 5" stroke="#fff" stroke-width="2" fill="none"/></svg></span>
</section>

<section class="builders" role="img" aria-label="Photograph of a warm wood kitchen interior">
  <h2 class="heading">OUR <span class="accent">BUILDERS</span></h2>
  <div class="builder" style="left:160px">
    <h3>BRIGHTLINE CUSTOM HOMES</h3>
    <span class="photo" role="img" aria-label="Builder showcase photo"></span>
    <p>Brightline Custom Homes at Ridgemere is quickly becoming the most sought custom home community. Opening soon, the first homesites are now offered to the public. These lots are ready for your own custom design and offer sweeping views.</p>
    <p>In order to take advantage of the pre development price, call now to secure a fully refundable deposit for a reservation of these lots.</p>
  </div>
  <div class="builder" style="left:668px">
    <h3>KEYSTONE RIDGE HOMES</h3>
    <span class="photo" role="img" aria-label="Builder showcase photo"></span>
    <p>Keystone Ridge Homes at Ridgemere is quickly becoming the most sought custom home community. Opening soon, the first homesites are now offered to the public. These lots are ready for your own custom design and offer sweeping views.</p>
    <p>In order to take advantage of the pre development price, call now to secure a fully refundable deposit for a reservation of these lots.</p>
  </div>
  <div class="cta"><span class="btn">BOOK NOW !</span></div>
  <p class="hurry">HURRY ONLY <span class="accent">THREE</span> CUSTOM LOTS ARE AVAILABLE!</p>
</section>

<section class="lifestyle">
  <h2 class="heading">LIFESTYLE</h2>
  <div class="script">Lorem ipsum is a dummy text</div>
  <div class="filters"><span class="active">All</span><span>Luxury Homes</span><span>Luxury Affordable</span><span>Community</span></div>
  <div class="gallery">
    <div class="photo" style="left:80px;top:220px;background:linear-gradient(180deg,#9ab4d0,#b8a890 60%,#6a7a58)" role="img" aria-label="Photo of a luxury home"></div>
    <div class="photo" style="left:346px;top:220px;background:linear-gradient(180deg,#7aa8d8,#e0e0e0 55%,#5a8a48)" role="img" aria-label="Photo of a white family home"></div>
    <div class="photo" style="left:612px;top:220px;background:linear-gradient(180deg,#6a88b0,#8a6a4a 55%,#3a4a38)" role="img" aria-label="Photo of a lodge home among pines"></div>
    <div class="photo" style="left:878px;top:220px;background:linear-gradient(180deg,#a8c8e0,#d8d0c0 50%,#3a9ab0)" role="img" aria-label="Photo of a resort pool"></div>
    <div class="photo" style="left:80px;top:420px;background:linear-gradient(180deg,#9ab4d0,#b8a890 60%,#6a7a58)" role="img" aria-label="Photo of a luxury home"></div>
    <div class="photo" style="left:346px;top:420px;background:linear-gradient(180deg,#7aa8d8,#e0e0e0 55%,#5a8a48)" role="img" aria-label="Photo of a white family home"></div>
    <div class="photo" style="left:612px;top:420px;background:linear-gradient(180deg,#6a88b0,#8a6a4a 55%,#3a4a38)" role="img" aria-label="Photo of a lodge home among pines"></div>
    <div class="photo" style="left:878px;top:420px;background:linear-gradient(180deg,#a8c8e0,#d8d0c0 50%,#3a9ab0)" role="img" aria-label="Photo of a resort pool"></div>
  </div>
</section>

<section class="enquiry" role="img" aria-label="Photograph of a couple meeting with an agent">
  <h2 class="heading">THERE'S NO BETTER <span class="accent">TIME</span> THAN NOW</h2>
  <div class="script">Get in touch, let's work together</div>
  <div class="form">
    <div class="field" style="top:0">Name</div>
    <div class="field" style="top:58px">E-Mail</div>
    <div class="field" style="top:116px">Phone</div>
    <div class="field message">Message</div>
  </div>
  <div class="cta"><span class="btn">CONTACT US</span></div>
</section>

<footer class="contact">
  <h2 class="heading">CONTACT <span class="accent">US</span></h2>
  <div class="social"><span></span><span></span><span></span><span></span><span></span></div>
  <p>555-014-2290 | <span class="accent">info@ridgemerehomes.com</span></p>
  <p>1420 Harlow Avenue, Fenwick, CA 90000</p>
</footer>

<footer class="legal">© 2016 <span class="accent">RIDGEMERE</span>. All Rights Reserved.</footer>

</body>
</html>
```